Vodka Bottle Label - Lune Vodka

I need a bottle label for a vodka I'd like to make called Lune Vodka.
I would like a label that looks elegant and fresh. I would like some mountains and colours to be red and white. Open to other colours being added but not too colourful. "Lune" means fresh, dawn in polish, i would like if mountains or something extra was added to the label too. I would like the Lune Vodka name not to be too small.
The vodka is made in australia and is 37%.

I would love to have a little bit of gold colour in the label!

I will provide the back label words when completing my decision.

i'd like to make it more simple and less european looking. More australian.

I saw a bottle like this and i did like the concept.

https://www.oakbarrelcellars.com.au/spirits/grey-vodka-range?srsltid=XqTz81mwkPLd04-hr-q7w93nfbzkgd_mR2yTpaMWxJeQ6vcbTnZsLpo

Target Market(s)

Vodka Drinkers

Industry/Entity Type

Alcohol

Colors
EB3D1F
EC4F4E
F09395
F8D3D4
FCEDEE

Requirements
Must have
• red and white colours incorporated, mountains or freshness on it.
Nice to have
• Fresh and clean look. Classy

```html
<!DOCTYPE html>
<html lang="en">
<head>
<meta charset="UTF-8">
<title>Lune Vodka – Bottle Label</title>
<link rel="stylesheet" href="https://fonts.googleapis.com/css2?family=Open+Sans:wght@300;400;700&display=swap">
<style>
  :root {
    --page-bg: #f6f1f1;
    --snow: #ffffff;
    --blush-faint: #fcedee;
    --blush-light: #f8d3d4;
    --blush-mid: #f09395;
    --coral: #ec4f4e;
    --brand-red: #eb3d1f;
    --gold: #c9a24a;
    --detail-ink: #3a2a2a;
  }
  html, body {
    margin: 0;
    padding: 0;
    width: 940px;
    height: 1200px;
    overflow: hidden;
    background: var(--page-bg);
    font-family: "Open Sans", sans-serif;
  }
  .label {
    position: absolute;
    left: 310px;
    top: 40px;
    width: 320px;
    height: 1120px;
    overflow: hidden;
    background: linear-gradient(90deg, var(--blush-faint) 0%, var(--snow) 14%, var(--snow) 86%, var(--blush-faint) 100%);
    box-shadow: 0 6px 24px rgba(120, 60, 60, 0.16);
  }
  .label__mountains {
    position: absolute;
    left: 0;
    right: 0;
    bottom: 0;
    height: 420px;
    background: linear-gradient(180deg, rgba(255,255,255,0) 0%, var(--blush-faint) 35%, var(--blush-light) 100%);
  }
  .label__frame {
    position: absolute;
    inset: 14px;
    border: 1.5px solid var(--gold);
    pointer-events: none;
  }
  .label__brand {
    position: absolute;
    left: 205px;
    top: 440px;
    transform: translate(-50%, -50%) rotate(-90deg);
    font-size: 178px;
    font-weight: 700;
    line-height: 1;
    letter-spacing: 4px;
    color: var(--brand-red);
    white-space: nowrap;
  }
  .label__details {
    position: absolute;
    right: 34px;
    top: 880px;
    text-align: right;
  }
  .label__type {
    margin: 0;
    font-size: 50px;
    font-weight: 300;
    letter-spacing: 1px;
    line-height: 1.1;
    color: var(--coral);
  }
  .label__rule {
    width: 70px;
    height: 2px;
    margin: 10px 0 0 auto;
    background: var(--gold);
  }
  .label__origin,
  .label__abv {
    margin: 0;
    font-size: 17px;
    font-weight: 400;
    line-height: 1.35;
    color: var(--detail-ink);
  }
  .label__origin { margin-top: 12px; }
</style>
</head>
<body>
  <main class="label">
    <div class="label__mountains" role="img" aria-label="Snow-capped mountain range at dawn in soft blush tones"></div>
    <div class="label__frame"></div>
    <div class="label__brand">LUNE</div>
    <div class="label__details">
      <p class="label__type">VODKA</p>
      <div class="label__rule"></div>
      <p class="label__origin">Made In Australia</p>
      <p class="label__abv">ALC. 37%VOL.</p>
    </div>
  </main>
</body>
</html>
```